Velvet Monsoon 2 EP - Album Cover ARTwork

I need an album cover ARTWORK for my new digital EP. Emphasis on the word ART ! It has to be artistic,creative & inspiring.NOT marketing stuff.It has to be minimal & clean.I make TRIBAL music which combines primitive\primal\ancient rhythms with new techy electronica.Listen here : https://tunewharf.example/kelpordaudio
kelpordaudio.example

Cover must include :
1.Title : Velvet Monsoon 2 EP
2.My logo ( attached )

Use your imagination,inspiration & design mastery to visualize VELVET MONSOON !

Digital Music

Digital

Must have
• 1.Title : Velvet Monsoon 2 EP
• 2.My logo ( attached )

```html
<!DOCTYPE html>
<html lang="en">
<head>
<meta charset="utf-8">
<title>Kelpord – Velvet Monsoon 2 EP</title>
<link href="https://fonts.googleapis.com/css2?family=Chewy&family=Michroma&display=swap" rel="stylesheet">
<style>
  :root {
    --ink-black: #000000;
    --title-yellow: #fff200;
    --logo-red: #e0452a;
    --ep-silver: #b9bcc0;
    --glow-gold: #f3d37a;
    --glow-orange: #e86a1c;
    --glow-red: #c3221a;
    --glow-blue: #2b6fb8;
    --glow-green: #4f8a3a;
  }
  html, body {
    margin: 0;
    padding: 0;
    overflow: hidden;
    background: var(--ink-black);
  }
  .cover {
    position: relative;
    width: 1200px;
    height: 1200px;
    overflow: hidden;
    background: var(--ink-black);
  }
  .cover-artwork {
    position: absolute;
    left: 180px;
    top: 0;
    width: 800px;
    height: 1200px;
    background:
      radial-gradient(ellipse 210px 210px at 58% 40%, rgba(90,60,70,0.95) 0%, rgba(60,40,40,0.9) 60%, rgba(243,211,122,0.85) 78%, rgba(0,0,0,0) 100%),
      radial-gradient(ellipse 280px 200px at 40% 66%, var(--glow-red) 0%, var(--glow-orange) 35%, rgba(195,34,26,0.5) 65%, rgba(0,0,0,0) 100%),
      radial-gradient(ellipse 120px 220px at 30% 55%, rgba(43,111,184,0.8) 0%, rgba(0,0,0,0) 100%),
      linear-gradient(to right, rgba(0,0,0,0) 30%, rgba(79,138,58,0.35) 42%, rgba(243,211,122,0.55) 55%, rgba(232,106,28,0.45) 68%, rgba(0,0,0,0) 80%);
    filter: blur(2px);
  }
  .band-name {
    position: absolute;
    left: 0;
    top: 60px;
    width: 1200px;
    margin: 0;
    text-align: center;
    font-family: "Chewy", cursive;
    font-weight: 400;
    font-size: 190px;
    line-height: 1;
    letter-spacing: 6px;
    color: var(--logo-red);
  }
  .release-title {
    position: absolute;
    left: 160px;
    top: 905px;
    margin: 0;
    font-family: "Chewy", cursive;
    font-weight: 400;
    color: var(--title-yellow);
    line-height: 0.92;
    text-transform: uppercase;
  }
  .release-title .line-one {
    display: block;
    font-size: 140px;
    padding-left: 80px;
    letter-spacing: 4px;
  }
  .release-title .line-two {
    display: block;
    font-size: 130px;
    letter-spacing: 2px;
  }
  .release-format {
    position: absolute;
    left: 976px;
    top: 1072px;
    font-family: "Michroma", sans-serif;
    font-size: 38px;
    color: var(--ep-silver);
    letter-spacing: 2px;
  }
</style>
</head>
<body>
  <main class="cover">
    <div class="cover-artwork" role="img" aria-label="Painted tribal totem with a round glowing-eyed mask disc, patterned red and orange panel, and streaks of gold, green and blue light"></div>
    <h2 class="band-name">Kelpord</h2>
    <h1 class="release-title">
      <span class="line-one">Velvet</span>
      <span class="line-two">Monsoon 2</span>
    </h1>
    <span class="release-format">EP</span>
  </main>
</body>
</html>
```